Company Website Re-design for Software development consultancy

We would like our company website to be redesigned using our existing marketing collateral and website content as a guide

current site : www.brovalex.com.au

For the different pages types and content please base on the following site : https://www.quorvantic.net/

We want a coded site - but will replace the content ourselves within the sections you provide to customise to our needs.

Target Market(s)

Medium to Large corporates needing software design and development services

Industry/Entity Type

Information Technology

Coding

Coded - Design and coding required

Number of Pages Required

5+ page

Font styles to use
Sans Serif

Colors
ec1f27
ffffff
000000

Requirements
Must have
• Align to colour scheme of existing collateral
• Include pages for the key areas of our busines - see : https://www.quorvantic.net/
Nice to have
• image rotators - make the site interesting to the business visitor

```html
<!DOCTYPE html>
<html lang="en">
<head>
<meta charset="utf-8">
<title>BROVALEX — Building Software Better</title>
<link rel="stylesheet" href="https://fonts.googleapis.com/css2?family=Montserrat:wght@500;600;700&family=Poppins:wght@400;500;600&family=Jost:wght@400;500&display=swap">
<style>
:root{
  --red:#ec1f27;
  --white:#ffffff;
  --black:#000000;
  --ink:#1a1a1a;
  --grey:#6b6b6b;
  --light:#9a9a9a;
  --dark:#1b1b1d;
}
*{margin:0;padding:0;box-sizing:border-box}
html,body{width:1200px;height:2908px;overflow:hidden;background:var(--white)}
body{position:relative;font-family:'Jost',sans-serif;color:var(--ink)}
.abs{position:absolute}
.center{left:0;width:100%;text-align:center}
.accent{color:var(--red)}

/* top bar */
.topbar{top:0;left:0;width:1200px;height:39px;background:var(--red)}
.topbar .social{left:0;top:0;width:482px;height:39px;background:var(--black);border-radius:0 20px 20px 0;display:flex;align-items:center;gap:16px;padding-left:76px}
.topbar .social span{width:11px;height:11px;border-radius:50%;background:var(--red)}
.topbar .contact{right:92px;top:0;height:39px;display:flex;align-items:center;gap:48px;color:var(--white);font-size:15px}
.topbar .contact div{display:flex;align-items:center;gap:10px}

/* nav */
.nav{top:39px;left:0;width:1200px;height:97px;background:var(--white)}
.brand{left:78px;top:30px;font-family:'Montserrat',sans-serif;font-weight:700;font-size:34px;letter-spacing:1px;color:var(--black)}
.menu{left:400px;top:38px;width:645px;display:flex;justify-content:space-between;font-family:'Poppins',sans-serif;font-size:14.5px;color:#555;white-space:nowrap}
.menu .active{color:var(--red);position:relative}
.menu .active::after{content:"";position:absolute;left:50%;top:30px;width:10px;height:3px;background:var(--black);transform:translateX(-50%)}
.search{left:1085px;top:30px;width:36px;height:36px;border-radius:50%;background:var(--black)}

/* hero */
.hero{top:136px;left:0;width:1200px;height:552px;overflow:hidden;background:linear-gradient(120deg,#3a3b3f 0%,#26272b 45%,#303236 70%,#1c1d20 100%)}
.hero .shade{inset:0;background:rgba(0,0,0,.35)}
.blob{border-radius:50%;background:var(--red);opacity:.55}
.hero-ring{left:544px;top:128px;width:112px;height:112px;border:5px solid var(--red);border-radius:50%}
.hero-name{top:262px;font-family:'Montserrat',sans-serif;font-weight:700;font-size:40px;letter-spacing:2px;color:var(--red)}
.hero-tag{top:330px;font-family:'Poppins',sans-serif;font-weight:500;font-size:22px;color:var(--white)}
.btn-ghost{left:527px;top:385px;width:146px;height:41px;border:2px solid var(--white);border-radius:22px;color:var(--white);font-family:'Poppins',sans-serif;font-weight:500;font-size:15px;display:flex;align-items:center;justify-content:center}
.dots{top:508px;left:0;width:100%;display:flex;justify-content:center;gap:7px;align-items:center}
.dots span{width:5px;height:5px;border-radius:50%;background:var(--white)}
.dots .on{width:16px;height:4px;border-radius:2px;background:var(--red)}

/* publish */
.publish{top:688px;left:0;width:1200px;height:417px}
.h2{font-family:'Montserrat',sans-serif;font-weight:600;font-size:27px;line-height:35px;color:var(--black);letter-spacing:.5px}
.lead{font-size:15px;line-height:27px;color:var(--grey)}
.publish .h2{top:58px}
.publish .lead{top:152px;left:240px;width:720px;text-align:center}
.btn{top:313px;height:41px;border-radius:22px;font-family:'Poppins',sans-serif;font-weight:500;font-size:15px;display:flex;align-items:center;justify-content:center}
.btn.outline{left:469px;width:126px;border:2px solid var(--red);color:var(--red)}
.btn.solid{left:605px;width:126px;background:var(--red);color:var(--white)}

/* faces */
.faces{top:1105px;left:0;width:1200px;height:614px;overflow:hidden;background:linear-gradient(110deg,#2a2a2c 0%,#1a1a1c 50%,#242427 100%)}
.faces .shade{inset:0;background:rgba(0,0,0,.45)}
.faces .h2{top:58px;color:var(--white)}
.faces .sub{top:118px;font-size:15px;color:var(--white)}
.tablet{left:78px;top:210px;width:446px;height:305px;border-radius:14px;background:linear-gradient(160deg,#2b2b2b,#0c0c0c);padding:14px}
.tablet .screen{width:100%;height:100%;background:linear-gradient(180deg,#f4f4f4,#dcdcdc);border-radius:4px}
.service-icon{width:86px;height:86px;border-radius:50%;border:4px solid var(--red);display:flex;align-items:center;justify-content:center;background:rgba(0,0,0,.25)}
.service-title{font-family:'Poppins',sans-serif;font-weight:600;font-size:16px;line-height:20px;color:var(--red)}
.service-text{font-size:15px;line-height:26px;color:var(--white)}

/* team */
.team{top:1719px;left:0;width:1200px;height:584px}
.team .h2{top:58px}
.team .lead{top:122px;left:230px;width:740px;text-align:center}
.member{top:228px;width:320px;text-align:center}
.member .photo{margin:0 auto;width:124px;height:124px;border-radius:50%;border:5px solid var(--red);background:linear-gradient(180deg,#c9c2bb,#7b7470)}
.member h4{margin-top:33px;font-family:'Poppins',sans-serif;font-weight:600;font-size:16px;color:var(--red)}
.member .role{margin-top:10px;font-size:15px;color:var(--ink)}
.member .bio{margin-top:10px;font-size:15px;line-height:27px;color:var(--grey)}
.member .in{position:absolute;left:151px;top:276px;width:18px;height:18px;background:#8a8a8a;border-radius:2px}

/* get started */
.start{top:2303px;left:0;width:1200px;height:333px;overflow:hidden;background:linear-gradient(100deg,#2c2c2f 0%,#17171a 60%,#2a2b2f 100%)}
.start .shade{inset:0;background:rgba(0,0,0,.45)}
.start .h2{top:58px;color:var(--white)}
.track{top:167px;height:4px}
.step{top:127px;width:85px;height:85px;border-radius:50%;border:4px solid var(--red);background:#151517;display:flex;align-items:center;justify-content:center}
.node{top:160px;width:19px;height:19px;border-radius:50%}
.step-label{top:228px;width:330px;text-align:center;font-size:14px;line-height:17px;color:var(--white)}

/* subscribe */
.subscribe{top:2636px;left:0;width:1200px;height:207px}
.subscribe h2{position:absolute;left:78px;top:54px;font-family:'Montserrat',sans-serif;font-weight:700;font-size:28px;color:var(--black)}
.subscribe .note{left:78px;top:122px;font-size:15px;color:var(--grey)}
.field{left:584px;top:108px;width:372px;height:40px;border-bottom:1px solid #d6d6d6;display:flex;align-items:center;justify-content:space-between;padding:0 8px 0 22px;font-size:14px;color:#444}

/* footer */
.footer{top:2843px;left:0;width:1200px;height:65px;background:var(--black);display:flex;align-items:center;justify-content:center;font-size:15px;color:var(--white)}
</style>
</head>
<body>

<header class="abs topbar">
  <div class="abs social" aria-label="Social links"><span></span><span></span><span></span></div>
  <div class="abs contact">
    <div>
      <svg width="14" height="18" viewBox="0 0 14 18"><path d="M7 0C3.1 0 0 3 0 6.9 0 12 7 18 7 18s7-6 7-11.1C14 3 10.9 0 7 0zm0 9.5A2.6 2.6 0 1 1 7 4.3a2.6 2.6 0 0 1 0 5.2z" fill="#000"/></svg>
      42 - 44 Harbour Ln, Sydney 2000
    </div>
    <div>
      <svg width="18" height="13" viewBox="0 0 18 13"><rect width="18" height="13" rx="1" fill="#000"/><path d="M1 1l8 6 8-6" stroke="#ec1f27" stroke-width="1.5" fill="none"/></svg>
      info@brovalex.com.au
    </div>
  </div>
</header>

<nav class="abs nav">
  <div class="abs brand">BROVALEX</div>
  <div class="abs menu">
    <span class="active">Home</span><span>About Us</span><span>Vellum Help</span><span>Vellum Micro - Services Platform</span><span>Contact Us</span>
  </div>
  <div class="abs search">
    <svg width="36" height="36" viewBox="0 0 36 36"><circle cx="16" cy="16" r="6" stroke="#ec1f27" stroke-width="2.5" fill="none"/><path d="M20.5 20.5l5 5" stroke="#ec1f27" stroke-width="2.5"/></svg>
  </div>
</nav>

<section class="abs hero">
  <div class="abs" style="inset:0" role="img" aria-label="Photo of a software team working at computer screens in an office"></div>
  <div class="abs shade"></div>
  <div class="abs blob" style="left:-210px;top:-40px;width:500px;height:500px"></div>
  <div class="abs blob" style="left:920px;top:230px;width:430px;height:430px"></div>
  <div class="abs hero-ring"></div>
  <div class="abs center hero-name">BROVALEX</div>
  <div class="abs center hero-tag">Building Software Better</div>
  <div class="abs btn-ghost">Contact Us</div>
  <div class="abs dots"><span></span><span class="on"></span><span></span></div>
</section>

<section class="abs publish">
  <h2 class="abs center h2">PUBLISH YOUR <span class="accent">MODELS</span> AS AN<br>ONLINE <span class="accent">SERVICE IN THE CLOUD</span></h2>
  <p class="abs lead">Vellum has been developed to enable Gridsheet-based financial and numerical models to be published securely and reliably without the need for a complex software development project.<br><br>The process of managing each version of your financial model is simple using our web portal, making usage tracking, support and maintainance easy.</p>
  <div class="abs btn outline">Learn More</div>
  <div class="abs btn solid">Get Started</div>
</section>

<section class="abs faces">
  <div class="abs" style="inset:0" role="img" aria-label="Photo of colleagues reviewing work together in a dim office"></div>
  <div class="abs shade"></div>
  <div class="abs blob" style="left:-260px;top:70px;width:620px;height:620px;opacity:.5"></div>
  <h2 class="abs center h2">THE THREE FACES OF <span class="accent">BROVALEX</span></h2>
  <div class="abs center sub">We are all about building software better.</div>
  <div class="abs tablet"><div class="screen" role="img" aria-label="Tablet showing a dashboard with charts and tables"></div></div>

  <div class="abs service-icon" style="left:564px;top:174px"><svg width="40" height="40" viewBox="0 0 40 40" fill="none" stroke="#fff" stroke-width="2"><circle cx="20" cy="20" r="7"/><circle cx="20" cy="5" r="3"/><circle cx="20" cy="35" r="3"/><circle cx="5" cy="20" r="3"/><circle cx="35" cy="20" r="3"/></svg></div>
  <h3 class="abs service-title" style="left:671px;top:176px">Consulting</h3>
  <p class="abs service-text" style="left:671px;top:204px;width:380px">Up-skill your team by using our consultants - for either short or long term engagements.</p>

  <div class="abs service-icon" style="left:603px;top:258px"><svg width="40" height="40" viewBox="0 0 40 40" fill="none" stroke="#fff" stroke-width="2"><rect x="6" y="8" width="28" height="24" rx="2"/><path d="M6 14h28M12 20l16 8M28 20l-16 8"/></svg></div>
  <h3 class="abs service-title" style="left:713px;top:312px">Projects</h3>
  <p class="abs service-text" style="left:713px;top:340px;width:430px">We can deliver a large project on a fixed price basis at a quality standard you won't believe</p>

  <div class="abs service-icon" style="left:657px;top:446px"><svg width="40" height="40" viewBox="0 0 40 40"><path d="M10 4h14l8 8v24H10z" fill="#fff"/><path d="M24 4v8h8" fill="#ccc"/><rect x="15" y="20" width="12" height="8" fill="#1b1b1d"/></svg></div>
  <h3 class="abs service-title" style="left:766px;top:448px">Vellum</h3>
  <p class="abs service-text" style="left:766px;top:476px;width:360px">Our product, Vellum, allows you to skip the development cycle and turn an gridsheet spreadsheet directly into either a web service or a web site</p>
</section>

<section class="abs team">
  <h2 class="abs center h2">MEET OUR <span class="accent">LEADERSHIP TEAM</span></h2>
  <p class="abs lead">Between just the partners, we have more than 60 years of software development experience. We combine a solid knowledge of computer science with a practical, pragmatic approach to delivering software.</p>
  <div class="abs member" style="left:78px">
    <div class="photo" role="img" aria-label="Portrait photo of a partner"></div>
    <h4>Ronan Pell</h4><div class="role">Partner</div>
    <div class="bio">Ronan's one of the best developers on the planet</div>
    <span class="in"></span>
  </div>
  <div class="abs member" style="left:439px">
    <div class="photo" role="img" aria-label="Portrait photo of a partner"></div>
    <h4>Miles Carrow</h4><div class="role">Partner</div>
    <div class="bio">Miles's been running software projects for 20 years</div>
    <span class="in"></span>
  </div>
  <div class="abs member" style="left:800px">
    <div class="photo" role="img" aria-label="Portrait photo of a partner"></div>
    <h4>Owen Tasker</h4><div class="role">Partner</div>
    <div class="bio">Owen codes for fun as much as he does for work</div>
    <span class="in"></span>
  </div>
</section>

<section class="abs start">
  <div class="abs" style="inset:0" role="img" aria-label="Photo of developers looking at code on monitors"></div>
  <div class="abs shade"></div>
  <div class="abs blob" style="left:-140px;top:160px;width:330px;height:330px;opacity:.5"></div>
  <div class="abs blob" style="left:1050px;top:-90px;width:300px;height:300px;opacity:.5"></div>
  <h2 class="abs center h2">GET <span class="accent">STARTED</span></h2>
  <div class="abs track" style="left:236px;width:363px;background:linear-gradient(90deg,var(--red) 0 52%,var(--white) 52%)"></div>
  <div class="abs track" style="left:599px;width:370px;background:linear-gradient(90deg,var(--white) 0 50%,var(--red) 50%)"></div>
  <div class="abs node" style="left:411px;background:var(--red)"></div>
  <div class="abs node" style="left:771px;background:var(--white)"></div>
  <div class="abs step" style="left:194px">
    <svg width="36" height="36" viewBox="0 0 36 36" fill="none" stroke="#fff" stroke-width="2"><circle cx="18" cy="18" r="14"/><ellipse cx="18" cy="18" rx="6" ry="14"/><path d="M4 18h28M7 10h22M7 26h22"/></svg>
  </div>
  <div class="abs step" style="left:557px">
    <svg width="36" height="36" viewBox="0 0 36 36" fill="none" stroke="#fff" stroke-width="2.5"><path d="M18 4v18M11 15l7 7 7-7M5 22v9h26v-9"/></svg>
  </div>
  <div class="abs step" style="left:927px">
    <svg width="38" height="36" viewBox="0 0 38 36" fill="none" stroke="#fff" stroke-width="2.5"><path d="M11 28H9a7 7 0 0 1 0-14 10 10 0 0 1 19-2 7.5 7.5 0 0 1 1 16h-2"/><path d="M19 32V18M14 23l5-5 5 5"/></svg>
  </div>
  <div class="abs step-label" style="left:71px">Create an account at <span class="accent">http://vellumhub.today</span></div>
  <div class="abs step-label" style="left:434px">Download and install the Vellum Add-in for<br><span class="accent">Gridsheet</span></div>
  <div class="abs step-label" style="left:804px">Build you models and publish to our <span class="accent">Cloud<br>Services</span></div>
</section>

<section class="abs subscribe">
  <h2>SUBSCRIBE <span class="accent">US!</span></h2>
  <div class="abs note">For latest news or updates subscribe our newsletter</div>
  <div class="abs field">
    <span>Enter e-mail*</span>
    <svg width="20" height="20" viewBox="0 0 20 20"><path d="M19 1L1 8l7 3 3 7z" fill="#ec1f27"/><path d="M19 1L8 11" stroke="#fff" stroke-width="1.2"/></svg>
  </div>
</section>

<footer class="abs footer"><span><span class="accent">© BROVALEX - 2018.</span> All Rights Reserved.</span></footer>

</body>
</html>
```